Super Greens Label for Supplement Bottle

We want to design a front label for a health supplement bottle. The product is called Meadow Twist Chews™. This will be a new product so there is no current website for the product. The focus is on supergreens that taste great and deliver support for energy, digestion, and immune defense.
We want it to be modern, vibrant and appealing.
Bottle size: standard size supplement CLEAR bottle size, with white child resistant cap and the label panel dimensions are 3” x 7”. The label should be primarily white and green, with a touch of red; (see color palettes)/it can also ONLY be white and green. See samples attached.
We are only focused on the front of the bottle design, not on the back, but leave space for the supplement panel and other text on the back.
So the text for the front of the bottle is:
RT Balden's
Meadow Twist Chews™
Super Greens Blend for:
Energy, Digestion, and Immune Support*
60 Gummies | Dietary Supplement
Raspberry Flavor Gummies
Off to side of the label:
Non-GMO
Vegan Friendly
Plant-Based
Gelatin Free
Colors
Designer to choose colors to be used in the design.

```html
<!DOCTYPE html>
<html lang="en">
<head>
<meta charset="utf-8">
<title>Meadow Twist Chews – Front Label</title>
<link href="https://fonts.googleapis.com/css2?family=Open+Sans:wght@400&family=Roboto+Condensed:wght@400;500&display=swap" rel="stylesheet">
<style>
  :root {
    --backdrop: #ebebeb;
    --olive: #7a9544;
    --leaf: #2f7a3a;
    --forest: #0f5a2a;
    --sea: #3f8a5e;
    --ink-light: #ffffff;
    --badge-line: #6fb04a;
    --berry: #8b1f3c;
  }
  * { margin: 0; padding: 0; box-sizing: border-box; }
  html, body { width: 1200px; height: 1200px; overflow: hidden; background: var(--backdrop); }
  .canvas { position: relative; width: 1200px; height: 1200px; }

  .label {
    position: absolute; left: 240px; top: 160px; width: 720px; height: 880px;
    background:
      radial-gradient(ellipse 60% 35% at 20% 10%, rgba(170,190,120,0.55), transparent 70%),
      radial-gradient(ellipse 55% 40% at 15% 62%, rgba(120,180,130,0.45), transparent 70%),
      linear-gradient(180deg, var(--olive) 0%, var(--leaf) 38%, var(--forest) 62%, var(--sea) 82%, var(--forest) 100%);
    color: var(--ink-light);
    text-align: center;
    overflow: hidden;
  }

  .brand {
    position: absolute; top: 70px; left: 0; right: 0;
    font-family: "Open Sans", sans-serif; font-weight: 400; font-size: 54px; letter-spacing: 0.5px;
  }
  .product-name {
    position: absolute; top: 215px; left: 40px; right: 0;
    font-family: "Roboto Condensed", sans-serif; font-weight: 500;
    font-size: 92px; line-height: 96px; letter-spacing: 1px; text-transform: uppercase;
  }
  .blend-lead {
    position: absolute; top: 475px; left: 40px; right: 0;
    font-family: "Roboto Condensed", sans-serif; font-size: 30px;
  }
  .benefits {
    position: absolute; top: 530px; left: 40px; right: 0;
    font-family: "Roboto Condensed", sans-serif; font-size: 26px; text-transform: uppercase;
  }
  .flavor {
    position: absolute; top: 625px; left: 40px; right: 0;
    font-family: "Roboto Condensed", sans-serif; font-size: 23px;
  }
  .flavor-art {
    position: absolute; top: 665px; left: 345px; width: 110px; height: 110px;
    border-radius: 50%;
    background: radial-gradient(circle at 50% 60%, rgba(139,31,60,0.75), rgba(139,31,60,0.2) 60%, transparent 72%);
  }
  .divider {
    position: absolute; top: 790px; left: 270px; width: 260px; height: 2px; background: var(--ink-light);
  }
  .count-line {
    position: absolute; top: 820px; left: 40px; right: 0;
    font-family: "Roboto Condensed", sans-serif; font-size: 27px;
  }

  .claims-strip {
    position: absolute; left: 0; top: 330px; width: 48px; height: 550px;
    background: var(--ink-light); border-radius: 0 24px 0 0;
  }
  .claims-strip svg { position: absolute; left: 0; top: 0; }
</style>
</head>
<body>
<main class="canvas">
  <section class="label" aria-label="Meadow Twist Chews front label">
    <div class="brand">RT Balden's</div>
    <h1 class="product-name">Meadow Twist<br>Chews™</h1>
    <p class="blend-lead">Super Greens Blend for:</p>
    <p class="benefits">Energy, Digestion &amp; Immune Support*</p>
    <p class="flavor">Raspberry Flavor Gummies</p>
    <div class="flavor-art" role="img" aria-label="Line drawing of raspberries with leaves"></div>
    <div class="divider"></div>
    <p class="count-line">60 Gummies &nbsp;|&nbsp; Dietary Supplement</p>

    <aside class="claims-strip" aria-label="Non-GMO, Vegan Friendly, Plant-Based, Gelatin Free">
      <svg width="48" height="550" viewBox="0 0 48 550">
        <g fill="none" stroke="var(--badge-line)" stroke-width="3">
          <circle cx="20" cy="90" r="20"/>
          <circle cx="20" cy="200" r="20"/>
          <circle cx="20" cy="310" r="20"/>
          <circle cx="20" cy="420" r="20"/>
        </g>
      </svg>
    </aside>
  </section>
</main>
</body>
</html>
```